PPT Template Graphic Design for Firm Serving Sales & Mrkting Executives in High-Tech Comopanies

Brookvane seeks a graphic design for a PowerPoint template for corporate presentations.
We are a workforce solutions company that specializes in finding and managing contractors for sales and marketing organizations in high-tech companies. We can also manage entire processes with our 'managed services' solution, for existing clients. We are unique in our exclusive focus on sales & marketing, our consultative approach that works with clients to leverage contractors, not just to fill immediate resource gaps they may have, but also to achieve immediate and longer term business goals of their organization. We offer the dual advantage of flexibility as clients may find within a boutique firm, and the scalability of a global company which means that regardless of whether clients need one contractor or several, locally or in foreign markets, we can help.
We will use this PPT template to present what we do to help clients, and how we are different from the competition to prospective clients. We might also use this PPT template to present proposals.
Updates

Project Deadline Extended
Reason: We would love to see some more design options! Also, we have guaranteed the project since we first posted. Thank you!

Target Market(s)

Executives in sales and marketing organizations of high tech companies, including VP of Sales, VP marketing, CEO, CFO and heads of HR departments.

Industry/Entity Type

Graphic Design

Requirements
Must have
• Template must be simple, elegant, classy. Please include a cover page, supporting pages (for content of presentation) and concluding ("Thank You") page. Design must include our logo & tagline (see attached), and provide recommendations for heading font, copy font and ‘bullet’ styles. Please locate company name on bottom right of template. Design should be in the same family of the look and feel of our website (www.brookvane-example.com). We would like the design to convey simplicity and elegance. We’d also like it to reflect the personality of our firm: friendly and approachable, with a high level of professionalism. Design should feel confident, and up-to-date in its look. Template must be both MAC and PC compatible.
Nice to have
• Same template developed for PPT, imported into a Prezi format as well. We need the PPT template for sure, but one in Prezi would be great to have as well - to enable more professional looking format for presentations.

```html
<!DOCTYPE html>
<html lang="en">
<head>
<meta charset="utf-8">
<title>Brookvane – Content Slide</title>
<link href="https://fonts.googleapis.com/css2?family=Arimo:wght@400;700&family=Oswald:wght@600&display=swap" rel="stylesheet">
<style>
  :root {
    --canvas: #ececec;
    --header-bar: #5f5f5f;
    --panel: #ffffff;
    --panel-border: #b9b9b9;
    --accent-orange: #f26a21;
    --accent-blue: #2196c9;
    --ink-dark: #1a1a1a;
    --brand-grey: #6b6b6b;
    --white: #ffffff;
    --art-start: #d7e9f3;
    --art-end: #fbe1d1;
  }
  * { margin: 0; padding: 0; box-sizing: border-box; }
  html, body { width: 1200px; height: 900px; overflow: hidden; }
  body {
    background: var(--canvas);
    font-family: "Arimo", Arial, sans-serif;
    position: relative;
  }
  .slide-header {
    position: absolute; left: 52px; top: 18px;
    width: 1110px; height: 96px;
    background: var(--header-bar);
    color: var(--white);
    text-align: right;
    padding: 14px 14px 0 0;
  }
  .slide-title {
    font-family: "Oswald", "Arial Narrow", sans-serif;
    font-weight: 600;
    font-size: 45px;
    line-height: 50px;
    letter-spacing: 0.5px;
  }
  .slide-subtitle {
    font-size: 20px;
    line-height: 24px;
    margin-top: 2px;
  }
  .content-panel {
    position: absolute; left: 52px; top: 134px;
    width: 1110px; height: 649px;
    background: var(--panel);
    border: 1px solid var(--panel-border);
  }
  .section-heading {
    position: absolute; left: 30px; top: 44px;
    width: 1008px; height: 44px;
    border-bottom: 2px solid var(--accent-orange);
    display: flex; align-items: flex-start;
  }
  .section-heading svg { width: 34px; height: 32px; margin-right: 14px; margin-top: 2px; }
  .section-heading h2 {
    color: var(--accent-orange);
    font-weight: 400;
    font-size: 30px;
    line-height: 36px;
  }
  .bullet-list {
    position: absolute; left: 40px; top: 116px;
    list-style: none;
  }
  .bullet-list li {
    display: flex; align-items: center;
    height: 56px;
    color: var(--accent-blue);
    font-size: 25px;
  }
  .bullet-list svg { width: 12px; height: 14px; margin-right: 26px; }
  .illustration-area {
    position: absolute; left: 780px; top: 173px;
    width: 180px; height: 308px;
    border-radius: 10px;
    background: linear-gradient(160deg, var(--art-start), var(--art-end));
  }
  .brand-block {
    position: absolute; right: 42px; top: 810px;
    display: flex; align-items: center;
  }
  .brand-mark {
    width: 54px; height: 54px; border-radius: 50%;
    background: var(--brand-grey);
    margin-right: 12px;
  }
  .brand-name {
    color: var(--brand-grey);
    font-size: 45px;
    line-height: 48px;
    font-weight: 400;
  }
  .brand-tagline {
    color: var(--brand-grey);
    font-size: 13.5px;
    line-height: 16px;
    letter-spacing: 0.3px;
  }
</style>
</head>
<body>
  <header class="slide-header">
    <h1 class="slide-title">PROJECT TITLE HERE</h1>
    <p class="slide-subtitle">Sub title here</p>
  </header>

  <main class="content-panel">
    <div class="section-heading">
      <svg viewBox="0 0 34 32" aria-hidden="true">
        <path d="M3 17 L12 27 L31 4" fill="none" stroke="var(--accent-orange)" stroke-width="6" stroke-linecap="square"/>
      </svg>
      <h2>Lorem ipsum dlolor sit ipsum ipsum</h2>
    </div>

    <ul class="bullet-list">
      <li><svg viewBox="0 0 12 14" aria-hidden="true"><path d="M2 2 L9 7 L2 12" fill="none" stroke="var(--ink-dark)" stroke-width="3"/></svg>Lorem ipsum dlolor sit ipsum ipsum</li>
      <li><svg viewBox="0 0 12 14" aria-hidden="true"><path d="M2 2 L9 7 L2 12" fill="none" stroke="var(--ink-dark)" stroke-width="3"/></svg>Lorem ipsum dlolor sit ipsum ipsum</li>
      <li><svg viewBox="0 0 12 14" aria-hidden="true"><path d="M2 2 L9 7 L2 12" fill="none" stroke="var(--ink-dark)" stroke-width="3"/></svg>Lorem ipsum dlolor sit ipsum ipsum</li>
      <li><svg viewBox="0 0 12 14" aria-hidden="true"><path d="M2 2 L9 7 L2 12" fill="none" stroke="var(--ink-dark)" stroke-width="3"/></svg>Lorem ipsum dlolor sit ipsum ipsum</li>
      <li><svg viewBox="0 0 12 14" aria-hidden="true"><path d="M2 2 L9 7 L2 12" fill="none" stroke="var(--ink-dark)" stroke-width="3"/></svg>Lorem ipsum dlolor sit ipsum ipsum</li>
      <li><svg viewBox="0 0 12 14" aria-hidden="true"><path d="M2 2 L9 7 L2 12" fill="none" stroke="var(--ink-dark)" stroke-width="3"/></svg>Lorem ipsum dlolor sit ipsum ipsum</li>
    </ul>

    <div class="illustration-area" role="img" aria-label="Illustration of two figures, one blue and one orange, shaking hands beneath a globe with a group of people"></div>
  </main>

  <footer class="brand-block">
    <div class="brand-mark" aria-hidden="true"></div>
    <div>
      <div class="brand-name">Brookvane</div>
      <div class="brand-tagline">Growing sales with skilled people</div>
    </div>
  </footer>
</body>
</html>
```